Criação de Papelaria Profissional para Beleza
" CLÍNICA DE ESTÉTICA COMPLETA, COM ÊNFASE EM ATENDIMENTO PRÊMIUM (salas exclusivas, máquinas próprias, ambiente aconchegante com forte conexão nordestina) Serviços ofertados: Estética corporal, facial, injetáveis e laser) SITE: https://brunelva.com.br/ "

```html
<!DOCTYPE html>
<html lang="pt-BR">
<head>
<meta charset="UTF-8">
<title>Brunelva — Cartão de Visita</title>
<link href="https://fonts.googleapis.com/css2?family=Cinzel:wght@400&family=Montserrat:wght@300;400;500&display=swap" rel="stylesheet">
<style>
  :root {
    --backdrop: #d07d73;
    --card-light: #f4e4e1;
    --card-coral: #d7857a;
    --coral-ink: #c9766c;
    --white-ink: #fdf1ee;
    --faint-mark: rgba(255, 240, 236, 0.14);
  }
  * { margin: 0; padding: 0; box-sizing: border-box; }
  html, body {
    width: 1200px; height: 1200px; overflow: hidden;
    background: var(--backdrop);
  }
  .stationery {
    position: relative; width: 1200px; height: 1200px;
    display: flex; flex-direction: column; align-items: center; justify-content: center;
    gap: 60px;
  }
  .card {
    position: relative; width: 760px; height: 430px; overflow: hidden;
    box-shadow: 0 18px 40px rgba(110, 40, 34, 0.22);
  }
  .card--front { background: var(--card-light); display: flex; align-items: center; justify-content: center; }
  .card--back { background: var(--card-coral); color: var(--white-ink); }

  .brand { display: flex; flex-direction: column; align-items: center; gap: 14px; }
  .brand__dot { width: 34px; height: 34px; border-radius: 50%; background: var(--coral-ink); }
  .brand__name {
    font-family: "Cinzel", serif; font-weight: 400; font-size: 40px;
    letter-spacing: 0.38em; padding-left: 0.38em; color: var(--coral-ink); line-height: 1;
  }
  .brand__tagline {
    font-family: "Montserrat", sans-serif; font-weight: 400; font-size: 11px;
    letter-spacing: 0.42em; text-transform: uppercase; color: var(--coral-ink);
  }
  .card--back .brand__dot { background: var(--white-ink); width: 28px; height: 28px; }
  .card--back .brand__name { color: var(--white-ink); font-size: 32px; }
  .card--back .brand__tagline { color: var(--white-ink); font-size: 9px; }

  .faint-mark {
    position: absolute; right: 70px; top: -40px; width: 340px; height: 340px;
    border-radius: 50%; background: var(--faint-mark);
  }
  .card--back .brand { position: absolute; right: 110px; top: 70px; gap: 11px; }

  .person { position: absolute; left: 56px; top: 62px; font-family: "Montserrat", sans-serif; }
  .person__name { font-size: 20px; font-weight: 500; letter-spacing: 0.06em; text-transform: uppercase; }
  .person__role { font-size: 11px; font-weight: 300; margin-top: 6px; letter-spacing: 0.04em; }

  .contacts {
    position: absolute; left: 56px; bottom: 62px; list-style: none;
    font-family: "Montserrat", sans-serif; font-size: 12px; font-weight: 300;
    display: flex; flex-direction: column; gap: 13px;
  }
  .contacts li { display: flex; align-items: center; gap: 10px; }
  .contacts svg { width: 14px; height: 14px; flex: none; }
  .contacts .dot { width: 12px; height: 12px; border-radius: 50%; border: 1.2px solid var(--white-ink); flex: none; margin: 0 1px; }

  .address {
    position: absolute; right: 56px; bottom: 62px; font-style: normal;
    font-family: "Montserrat", sans-serif; font-size: 12px; font-weight: 300; line-height: 1.75;
  }
</style>
</head>
<body>
<main class="stationery">
  <section class="card card--front" aria-label="Frente do cartão">
    <div class="brand">
      <span class="brand__dot"></span>
      <span class="brand__name">BRUNELVA</span>
      <span class="brand__tagline">Clínica de Estética</span>
    </div>
  </section>

  <section class="card card--back" aria-label="Verso do cartão">
    <span class="faint-mark"></span>
    <div class="person">
      <p class="person__name">Tiago Moreira</p>
      <p class="person__role">Diretor Geral</p>
    </div>
    <ul class="contacts">
      <li>
        <svg viewBox="0 0 24 24" fill="none" stroke="#fdf1ee" stroke-width="1.8" stroke-linecap="round" stroke-linejoin="round"><path d="M5 3h4l2 5-2.5 1.5a11 11 0 0 0 6 6L16 13l5 2v4a2 2 0 0 1-2 2A17 17 0 0 1 3 5a2 2 0 0 1 2-2z"/></svg>
        (84) 99120-4417
      </li>
      <li><span class="dot"></span>@brunelvaestetica</li>
      <li>brunelva.com.br</li>
    </ul>
    <div class="brand">
      <span class="brand__dot"></span>
      <span class="brand__name">BRUNELVA</span>
      <span class="brand__tagline">Clínica de Estética</span>
    </div>
    <address class="address">
      Av. das Jandaias, 2150<br>
      Vila Serena – Porto Caiçá – RN<br>
      Salas 1201 a 1203
    </address>
  </section>
</main>
</body>
</html>
```